Dog breeder design card

A card for our dog showing/breeding and companion puppy buyers.
Updates

Project Deadline Extended
Reason: The photo's I provided were not seen by designers because of a glitch or error, so I will need to start them over again in the designs submitted to me. I uploaded and emailed the photo's last night.

Thank you all so much for your lovely designs, I like wquite a few of them. I provided images in my original brief, but these apparently did not become available for you to see. I have emailed my images now, so hopefully you may be able to incorporate them into your designs.

Thank you so much for your time,
kind regards,
Beatrice

I have attached the photo’s that can hopefully be incorporated onto my business card. I don’t mind if the whole images aren’t used, but maybe a soft focus look around the adult dog and in a corner of the card maybe....if that’s possible.

Contact Information for Business Card

Kestamor Bullmastiffs, adored by Gerald and Beatrice Lindqvist.
Wyndarra NSW
0497 358614

Requirements
Nice to have
• Soft focus look to the outline of adult dogs head incorporated into perhaps a corner of the card. Soft focus outline around pups perhaps.
I do really love hot pink and/or purple text if possible.
"Kestamor Bullmastiffs" to be incorporated on the front of card, our details on reverse.
Would prefer a glossy finish rather than matt.

```html
<!DOCTYPE html>
<html lang="en">
<head>
<meta charset="utf-8">
<title>Kestamor Bullmastiffs — Business Card</title>
<link rel="stylesheet" href="https://fonts.googleapis.com/css2?family=Didact+Gothic&display=swap">
<style>
  :root {
    --backdrop: #ececec;
    --card-front: #d5d5d7;
    --card-back: #ffffff;
    --band: #d3d3d3;
    --hot-pink: #e6147f;
    --pink-soft: rgba(230, 20, 127, 0.22);
    --pink-faint: rgba(230, 20, 127, 0.06);
    --grey-soft: rgba(170, 170, 170, 0.35);
    --grey-faint: rgba(170, 170, 170, 0.05);
    --shadow: rgba(0, 0, 0, 0.18);
  }
  * { box-sizing: border-box; margin: 0; padding: 0; }
  html, body {
    width: 1200px;
    height: 900px;
    overflow: hidden;
    background: var(--backdrop);
    font-family: "Didact Gothic", "Century Gothic", sans-serif;
  }
  .card {
    position: absolute;
    width: 600px;
    height: 343px;
    box-shadow: 0 6px 18px var(--shadow);
  }

  /* Front */
  .card--front {
    left: 520px;
    top: 90px;
    background: var(--card-front);
  }
  .brand-name {
    font-weight: 400;
    color: var(--hot-pink);
    font-size: 56px;
    line-height: 1;
    letter-spacing: 0.5px;
  }
  .brand-name__line {
    position: absolute;
    white-space: nowrap;
  }
  .brand-name__line--first { left: 36px; top: 112px; }
  .brand-name__line--second { left: 96px; top: 182px; }
  .dog-artwork--front {
    position: absolute;
    left: 290px;
    top: 92px;
    width: 170px;
    height: 74px;
    border-radius: 40px 40px 8px 8px;
    background: radial-gradient(ellipse at center, var(--pink-soft), var(--pink-faint) 75%);
  }

  /* Back */
  .card--back {
    left: 80px;
    top: 470px;
    background: var(--card-back);
  }
  .dog-artwork--back {
    position: absolute;
    left: 74px;
    top: 48px;
    width: 200px;
    height: 88px;
    border-radius: 44px 44px 6px 6px;
    background: radial-gradient(ellipse at center, var(--grey-soft), var(--grey-faint) 75%);
  }
  .adored-by {
    position: absolute;
    left: 256px;
    top: 118px;
    color: var(--hot-pink);
    font-size: 15px;
  }
  .detail-band {
    position: absolute;
    left: 44px;
    width: 480px;
    height: 42px;
    background: var(--band);
    color: var(--hot-pink);
    font-size: 27px;
    line-height: 42px;
    padding-left: 6px;
    white-space: nowrap;
  }
  .detail-band--names { top: 140px; }
  .detail-band--contact { top: 204px; }
</style>
</head>
<body>
  <section class="card card--front" aria-label="Card front">
    <h1 class="brand-name">
      <span class="brand-name__line brand-name__line--first">Kestamor</span>
      <span class="brand-name__line brand-name__line--second">Bullmastiffs</span>
    </h1>
    <div class="dog-artwork dog-artwork--front" role="img" aria-label="Pink line outline of an adult bullmastiff head with a pup beside it"></div>
  </section>

  <section class="card card--back" aria-label="Card back">
    <div class="dog-artwork dog-artwork--back" role="img" aria-label="Faint soft-focus grey outline of an adult bullmastiff head with a pup"></div>
    <p class="adored-by">adored by</p>
    <p class="detail-band detail-band--names">Gerald and Beatrice Lindqvist</p>
    <p class="detail-band detail-band--contact">Wyndarra NSW 0497 358614</p>
  </section>
</body>
</html>
```